Tarvimoor business cards

Need fresh design for our business cards. Logo must be specific, we are open for everything else.

Contact Information for Business Card

phrase "GMP & JANITORIAL SERVICES" should be used as main point of card

Colors
3176b5
3276b5
85acd3
cedeed
ffffff
0292cd
33a6d7
85cae6
cee9f5

Requirements
Must have
• The logo
Should not have
• crowded designs

```html
<!DOCTYPE html>
<html lang="en">
<head>
<meta charset="utf-8">
<title>Tarvimoor Business Cards</title>
<link href="https://fonts.googleapis.com/css2?family=Lato:wght@400;700&display=swap" rel="stylesheet">
<style>
  :root {
    --stage: #2a2a2a;
    --brand-blue: #1479c4;
    --brand-light: #33a6d7;
    --sky-top: #2f9ad8;
    --sky-mid: #5ab4e4;
    --sky-deep: #1d86cc;
    --paper: #ffffff;
  }
  * { margin: 0; padding: 0; box-sizing: border-box; }
  html, body {
    width: 1200px; height: 1200px; overflow: hidden;
    background: var(--stage);
    font-family: "Lato", sans-serif;
  }
  .card {
    position: absolute;
    left: 110px;
    width: 980px; height: 540px;
    border-radius: 34px;
    overflow: hidden;
  }
  .card-front { top: 45px; }
  .card-back { top: 615px; background: var(--paper); color: var(--brand-blue); }

  .front-surface {
    position: absolute; inset: 0;
    background:
      radial-gradient(ellipse at 80% 70%, rgba(255,255,255,0.22), transparent 55%),
      radial-gradient(ellipse at 20% 20%, rgba(255,255,255,0.18), transparent 50%),
      linear-gradient(135deg, var(--sky-top) 0%, var(--sky-mid) 45%, var(--sky-deep) 100%);
  }
  .front-lockup {
    position: absolute; left: 0; right: 0; top: 215px;
    display: flex; flex-direction: column; align-items: center;
    color: var(--paper);
  }
  .front-name {
    font-size: 72px; font-weight: 400; letter-spacing: 14px;
    line-height: 1; padding-left: 14px;
  }
  .front-tagline {
    margin-top: 16px;
    font-size: 17px; font-weight: 700; letter-spacing: 5px;
    padding-left: 5px;
  }

  .edge-tab {
    position: absolute; left: 0; top: 62px;
    width: 20px; height: 48px;
    background: var(--brand-blue);
  }
  .person { position: absolute; left: 72px; top: 58px; }
  .person-name { font-size: 40px; font-weight: 700; letter-spacing: 0.5px; line-height: 1; }
  .person-role {
    margin-top: 8px;
    font-size: 19px; letter-spacing: 2.5px;
    color: var(--brand-light);
  }
  .back-lockup {
    position: absolute; right: 60px; top: 128px;
    display: flex; flex-direction: column; align-items: flex-end;
    color: var(--brand-blue);
  }
  .back-name {
    font-size: 64px; font-weight: 400; letter-spacing: 11px;
    line-height: 1; margin-right: -11px;
  }
  .back-tagline {
    margin-top: 14px;
    font-size: 15px; font-weight: 700; letter-spacing: 4.5px;
    margin-right: -4.5px;
  }
  .divider {
    position: absolute; left: 110px; right: 60px; top: 318px;
    height: 2px; background: var(--brand-blue);
  }
  .contacts {
    position: absolute; left: 80px; top: 350px;
    list-style: none; font-size: 23px; line-height: 40px;
  }
  .contacts li { display: flex; align-items: center; gap: 16px; }
  .contacts svg { width: 22px; height: 22px; fill: none; stroke: var(--brand-blue); stroke-width: 2; }
  .address {
    position: absolute; right: 60px; top: 350px;
    text-align: right; font-style: normal;
    font-size: 23px; line-height: 36px;
  }
</style>
</head>
<body>

<section class="card card-front">
  <div class="front-surface" role="img" aria-label="Faceted blue geometric background"></div>
  <div class="front-lockup">
    <div class="front-name">TARVIMOOR</div>
    <div class="front-tagline">GMP &amp; JANITORIAL SERVICES</div>
  </div>
</section>

<section class="card card-back">
  <div class="edge-tab"></div>
  <div class="person">
    <div class="person-name">MARCUS HALE</div>
    <div class="person-role">MANAGING DIRECTOR</div>
  </div>
  <div class="back-lockup">
    <div class="back-name">TARVIMOOR</div>
    <div class="back-tagline">GMP &amp; JANITORIAL SERVICES</div>
  </div>
  <div class="divider"></div>
  <ul class="contacts">
    <li>
      <svg viewBox="0 0 24 24"><path d="M5 3h4l2 5-3 2a12 12 0 0 0 6 6l2-3 5 2v4a2 2 0 0 1-2 2A18 18 0 0 1 3 5a2 2 0 0 1 2-2z"/></svg>
      214-555-0187
    </li>
    <li>
      <svg viewBox="0 0 24 24"><rect x="2" y="5" width="20" height="14"/><path d="M2 5l10 8 10-8"/></svg>
      marcus@tarvimoor.com
    </li>
    <li>
      <svg viewBox="0 0 24 24"><circle cx="12" cy="12" r="10"/><path d="M2 12h20M12 2c3 3 3 17 0 20M12 2c-3 3-3 17 0 20"/></svg>
      www.tarvimoor.com
    </li>
  </ul>
  <address class="address">
    418 Larkspur Street<br>
    Suite 210, Fenwick Falls<br>
    MI 49217
  </address>
</section>

</body>
</html>
```